Stylish new business card needed!

Hello everyone! I am in need of a new business card design for an alarm company here in Hurricane WV. I have all fonts, color codes and logos provided for you use! We are a young company and like the style of a clean sleek looking business card. Would like it double sided, one side holding the logo and the other with your design!
Target Market(s)
The people that are looking for the newest tech for home automation and security
Industry/Entity Type
Alarm services; Home automation
Contact Information for Business Card
Name of person; position (Sales; Installer); Phone Number (555.419.7362); Employee cell Number; Website (www.GuardedByVelm.example); Employee Email; Double sided
Look and feel
Each slider illustrates characteristics of the customer's brand and the style your logo design should communicate.

```html
<!DOCTYPE html>
<html lang="en">
<head>
<meta charset="utf-8">
<title>Velm Business Card</title>
<link rel="stylesheet" href="https://fonts.googleapis.com/css2?family=Montserrat:wght@400;500;600&display=swap">
<style>
  :root {
    --backdrop: #3b3b3b;
    --card-white: #ffffff;
    --card-black: #151515;
    --brand-orange: #f7904a;
    --brand-gray: #9b9b9b;
    --ink: #1f1f1f;
    --ink-soft: #3a3a3a;
  }
  * { box-sizing: border-box; margin: 0; padding: 0; }
  html, body {
    width: 1200px;
    height: 1200px;
    overflow: hidden;
    background: var(--backdrop);
    font-family: "Montserrat", Arial, sans-serif;
  }
  .stage {
    position: relative;
    width: 1200px;
    height: 1200px;
  }
  .card {
    position: absolute;
    left: 250px;
    width: 700px;
    height: 400px;
    border-radius: 34px;
    overflow: hidden;
    box-shadow: 0 18px 40px rgba(0, 0, 0, 0.45);
  }
  .card--front { top: 180px; background: var(--card-white); }
  .card--back { top: 620px; background: var(--card-black); }

  .wordmark {
    position: absolute;
    font-weight: 500;
    color: var(--brand-gray);
    letter-spacing: 0.04em;
    line-height: 1;
  }
  .card--front .wordmark { right: 70px; top: 70px; font-size: 96px; }
  .card--back .wordmark {
    left: 0; right: 0; top: 50%;
    transform: translateY(-50%);
    text-align: center;
    font-size: 150px;
  }

  .identity {
    position: absolute;
    left: 70px;
    top: 205px;
  }
  .identity__name {
    font-size: 28px;
    font-weight: 600;
    color: var(--brand-orange);
    letter-spacing: 0.01em;
    line-height: 1;
  }
  .identity__role {
    font-size: 15px;
    font-weight: 500;
    color: var(--ink-soft);
    letter-spacing: 0.02em;
    margin-top: 4px;
  }
  .contacts {
    list-style: none;
    margin-top: 12px;
  }
  .contacts li {
    display: flex;
    align-items: center;
    gap: 12px;
    font-size: 17px;
    color: var(--ink);
    height: 25px;
  }
  .contacts svg { width: 18px; height: 18px; flex: none; }

  .band-orange {
    position: absolute;
    left: 0; bottom: 0;
    width: 60%;
    height: 14px;
    background: var(--brand-orange);
  }
  .band-gray {
    position: absolute;
    right: 0; bottom: 0;
    width: calc(40% - 8px);
    height: 28px;
    background: var(--brand-gray);
  }
</style>
</head>
<body>
<main class="stage">
  <section class="card card--front" aria-label="Business card front">
    <div class="wordmark">VELM</div>
    <div class="identity">
      <p class="identity__name">FULL NAME</p>
      <p class="identity__role">POSITION</p>
      <ul class="contacts">
        <li>
          <svg viewBox="0 0 24 24" aria-hidden="true"><path fill="#f7904a" d="M6.6 10.8a15.1 15.1 0 0 0 6.6 6.6l2.2-2.2a1 1 0 0 1 1-.25 11.4 11.4 0 0 0 3.6.57 1 1 0 0 1 1 1V20a1 1 0 0 1-1 1A17 17 0 0 1 3 4a1 1 0 0 1 1-1h3.5a1 1 0 0 1 1 1c0 1.25.2 2.45.57 3.57a1 1 0 0 1-.25 1z"/></svg>
          555.419.7362
        </li>
        <li>
          <svg viewBox="0 0 24 24" aria-hidden="true"><rect x="6" y="2" width="12" height="20" rx="2" fill="none" stroke="#f7904a" stroke-width="2"/><circle cx="12" cy="18" r="1.2" fill="#f7904a"/></svg>
          555.419.7362
        </li>
        <li>
          <svg viewBox="0 0 24 24" aria-hidden="true"><rect x="2" y="5" width="20" height="14" fill="#f7904a"/><path d="M2 5l10 8 10-8" fill="none" stroke="#fff" stroke-width="1.6"/></svg>
          email@company.com
        </li>
        <li>
          <svg viewBox="0 0 24 24" aria-hidden="true"><g fill="none" stroke="#f7904a" stroke-width="1.8"><circle cx="12" cy="12" r="9.5"/><ellipse cx="12" cy="12" rx="4" ry="9.5"/><path d="M2.5 12h19M4 7h16M4 17h16"/></g></svg>
          www.GuardedByVelm.example
        </li>
      </ul>
    </div>
    <div class="band-orange"></div>
    <div class="band-gray"></div>
  </section>

  <section class="card card--back" aria-label="Business card back">
    <div class="wordmark">VELM</div>
  </section>
</main>
</body>
</html>
```